Young Adult novel ebook design

The book is called Label Whore: Inspired By A True StoryIt's about a wealthy male teenager who is too much into appearances, but is later humbled by a seriea of events. I need a trendy cover that resembles other top Young Adult covers, such as the examples attached. But something unique that stands out.
Target Market(s)
Teens, young adult, middle schoolers, high schoolers
Industry/Entity Type
Writer
Colors
Designer to choose colors to be used in the design.
Requirements
Must have
- Be creative and eye catching for a teenager. Leave space for the author's name. Will reveal the name to the winner.
Nice to have
- Get inspired by some of the example covers I attached.
Should not have
- No images that clearly shows a person's race. The main character image should be up for interpretation.

```html
<!DOCTYPE html>
<html lang="en">
<head>
<meta charset="utf-8">
<title>Tassel Glutton — Cover</title>
<link href="https://fonts.googleapis.com/css2?family=Gochi+Hand&display=swap" rel="stylesheet">
<style>
  :root {
    --stage: #e4e8e9;
    --cover-black: #050505;
    --photo-dark: #0c0c0c;
    --photo-mid: #6a6a6a;
    --photo-light: #bdbdbd;
    --ink-light: #e6e6e6;
  }
  * { margin: 0; padding: 0; box-sizing: border-box; }
  html, body {
    width: 1200px;
    height: 1000px;
    overflow: hidden;
    background: var(--stage);
  }
  .cover {
    position: absolute;
    left: 276px;
    top: 40px;
    width: 648px;
    height: 920px;
    background: var(--cover-black);
    overflow: hidden;
    font-family: "Gochi Hand", cursive;
    color: var(--ink-light);
  }
  .cover-photo {
    position: absolute;
    left: 0;
    top: 0;
    width: 270px;
    height: 920px;
    background:
      radial-gradient(ellipse 120px 260px at 215px 380px, var(--photo-light) 0%, var(--photo-mid) 45%, transparent 100%),
      radial-gradient(ellipse 170px 300px at 110px 300px, var(--photo-mid) 0%, #2a2a2a 55%, transparent 100%),
      linear-gradient(90deg, var(--photo-dark) 0%, #1c1c1c 60%, var(--cover-black) 100%);
  }
  .title {
    position: absolute;
    left: 222px;
    top: 150px;
    font-size: 132px;
    line-height: 0.95;
    font-weight: 400;
    letter-spacing: 1px;
  }
  .title span { display: block; }
  .subtitle {
    position: absolute;
    left: 238px;
    top: 528px;
    font-size: 27px;
    letter-spacing: 0.5px;
  }
  .author {
    position: absolute;
    left: 0;
    width: 100%;
    padding-left: 120px;
    text-align: center;
    top: 780px;
    font-size: 44px;
  }
</style>
</head>
<body>
  <main class="cover">
    <div class="cover-photo" role="img" aria-label="Black and white portrait of a young man half hiding his face behind his raised hand"></div>
    <h1 class="title"><span>tassel</span><span>glutton</span></h1>
    <p class="subtitle">drawn from a real season</p>
    <p class="author">author's name</p>
  </main>
</body>
</html>
```